The Busy Wren Organic & Natural Soaps is looking for label designs (along with the business card proje

This is my scope and requirements:
Labelling project:
This is related to the Label project I also opened up. (The Busy Wren Organic & Natural Soaps needs a good business card (Contest) )
I have attached an initial draft at a logo I tried to come up with for a business card and labelling/marketing. I am hoping that you can take this logo and 'run with it' to finesse it, make it look unique and professional. If you need to change it, I am open to ideas.
I find that labelling/packaging is hard for me to make it look 'professional' so I am coming to the experts!
I am looking for label designs for 2 different bottles and 2 different bar soaps:
1) Organic Bar Soap (2 possibilities: 1) Kraft 'cigar' band around soap with twine, 2) Kraft soap box with Kraft sticker Labels
2) Natural Olive Oil Based Bar Soap (labelling can be same as Organic but with distinct info)
3) Organic Hand Washes (clear square bottles, 250ml with natural pump)
4) Natural Olive Oil Based Body Wash (taper bottle 200ml with metal silver disc top caps)
I am a start up at home company making Organic and Natural Bar soaps, hand soaps, body washes.
All of my ingredients are organic or natural and will include natural essential oils, exfoliants, natural powders/colours, etc.
Some of the names are: Brisquel (feisty, energetic soap), Dunmoor (more of a sandalwood earthy tones with a sandalwood powder exfoliant), Frosk (maybe changing this name - fresh scented), Plum Cardamom (lemongrass/ginger, exfoliants), etc....
If you need more information, please let me know!
Please find attached: Kraft Paper I am looking at to possibly wrap the Bar Soaps in (I like the different colour concept and am trying to decide between diff colours of Wendell Prask paper to wrap around or plain kraft paper.. whichever the new logo concept will look best with.
The bottles I will be using for the hand soap (250ml square) and the body wash (200ml tapered)
OLD POST:
Hello! I am a start up business that is specializing in making luxury organic bar soaps, natural olive oil bar soaps, organic hand wash, natural olive oil body wash/shower gel that will include essential oils, exfoliants, natural powders, etc. (also accessories: wood soap dishes, etc) .. I am looking for a great designer that can provide me with the business card and labelling designs! I appreciate feedback, ideas on how I can receive a great design to help sell my products!
I am attaching my initial logo design that I would like to keep - but am looking for someone to 'finesse' it or make it more professional/unique looking.
Again, this is hand in hand with the business card project I submitted.
Thanks!
Mirela
Updates
I am sorry for the lack of direction or Scope of the project. I am new at this board.
Labelling project:
I have attached an initial draft at a logo I tried to come up with for a business card and labelling/marketing. I am hoping that you can take this logo and 'run with it' to finesse it, make it look unique and professional.
If you need more information, please let me know.
Hello; I just wanted to let everyone know that if you feel that this brand needs a different logo, I am open to ideas (if you don't think the one I started with is ok). I am coming to the experts here!
Just to confirm also - this is related to the business card project, therefore, there are 2 projects, 2 payments! :)
Cheers

```html
<!DOCTYPE html>
<html lang="en">
<head>
<meta charset="utf-8">
<title>The Busy Wren – Hand Wash Label and Soap Band</title>
<link href="https://fonts.googleapis.com/css2?family=Lilita+One&family=Short+Stack&display=swap" rel="stylesheet">
<style>
  :root {
    --page: #ffffff;
    --label-bg: #e6e7e9;
    --label-frame: #b9bbbe;
    --slate: #889eab;
    --charcoal: #555557;
    --white: #ffffff;
    --lime: #e2ebb7;
    --band-strip: #bcbcbc;
    --dot-gold: #e8c766;
    --dot-rose: #e58a93;
    --dot-white: #f2f4f5;
  }
  * { box-sizing: border-box; margin: 0; padding: 0; }
  html, body { width: 1200px; height: 850px; overflow: hidden; background: var(--page); }
  .canvas { position: relative; width: 1200px; height: 850px; }

  .display { font-family: "Lilita One", "Arial Black", sans-serif; }
  .handwritten { font-family: "Short Stack", "Comic Sans MS", cursive; }

  /* Hand wash bottle label */
  .bottle-label {
    position: absolute; left: 162px; top: 260px; width: 200px; height: 436px;
    background: var(--label-bg); border: 7px solid var(--label-frame); border-radius: 16px;
    overflow: hidden;
  }
  .bottle-label .brand-name {
    position: absolute; left: 0; right: 0; top: 54px; text-align: center;
    color: var(--charcoal); font-size: 40px; line-height: 42px; letter-spacing: 0.5px;
  }
  .bottle-label .divider {
    position: absolute; left: 8px; right: 8px; height: 0; border-top: 2px dotted;
  }
  .bottle-label .divider--gold { top: 168px; border-color: var(--dot-gold); }
  .bottle-label .divider--rose { top: 241px; border-color: var(--dot-rose); }
  .bottle-label .range {
    position: absolute; left: 0; right: 0; top: 182px; text-align: center;
    color: var(--slate); font-size: 15px; line-height: 29px; text-transform: uppercase;
  }
  .bottle-label .scent-badge {
    position: absolute; left: 6px; bottom: 0; width: 176px; height: 134px;
  }

  /* Olive oil soap band */
  .soap-band {
    position: absolute; left: 685px; top: 312px; width: 515px; height: 288px;
    background: var(--lime);
  }
  .soap-band .strip {
    position: absolute; left: 0; right: 0; top: 54px; height: 169px;
    background: var(--slate); border-top: 10px solid var(--band-strip); border-bottom: 10px solid var(--band-strip);
  }
  .soap-band .brand-name {
    position: absolute; left: 34px; top: 84px; width: 120px; text-align: center;
    color: var(--white); font-size: 32px; line-height: 36px;
  }
  .soap-band .divider {
    position: absolute; left: 34px; width: 120px; top: 187px; border-top: 2px dotted var(--dot-white);
  }
  .soap-band .product-type {
    position: absolute; left: 34px; width: 124px; top: 202px; text-align: center;
    color: var(--charcoal); font-size: 12px; text-transform: uppercase;
  }
  .soap-band .scent-badge {
    position: absolute; right: 4px; top: 80px; width: 196px; height: 143px;
  }

  .scent-badge svg { position: absolute; inset: 0; width: 100%; height: 100%; }
  .scent-badge .scent-name {
    position: absolute; left: 0; right: 0; text-align: center; font-size: 24px; text-transform: uppercase;
  }
  .scent-badge .scent-note {
    position: absolute; left: 0; right: 0; text-align: center; font-size: 14px; line-height: 19px; text-transform: uppercase;
  }
  .bottle-label .scent-name { top: 56px; color: var(--white); font-size: 22px; }
  .bottle-label .scent-note { top: 88px; color: var(--charcoal); font-size: 12.5px; line-height: 18px; }
  .soap-band .scent-name { top: 54px; color: var(--charcoal); }
  .soap-band .scent-note { top: 92px; color: var(--slate); font-size: 15px; line-height: 21px; }
</style>
</head>
<body>
<main class="canvas">

  <section class="bottle-label" aria-label="Organic hand wash bottle label">
    <p class="brand-name display">THE BUSY<br>WREN</p>
    <div class="divider divider--gold"></div>
    <p class="range display">Organic<br>Hand Washes</p>
    <div class="divider divider--rose"></div>
    <div class="scent-badge">
      <svg viewBox="0 0 176 134" preserveAspectRatio="none" aria-hidden="true">
        <path d="M0,134 C2,78 40,42 100,34 C132,30 148,16 158,0 C150,32 176,60 176,134 Z" fill="var(--slate)"/>
      </svg>
      <p class="scent-name display">Dunmoor</p>
      <p class="scent-note handwritten">Feisty<br>Energetic Soap</p>
    </div>
  </section>

  <section class="soap-band" aria-label="Olive oil soap wrap band">
    <div class="strip"></div>
    <p class="brand-name display">THE BUSY<br>WREN</p>
    <div class="divider"></div>
    <p class="product-type display">Olive Oil Soap</p>
    <div class="scent-badge">
      <svg viewBox="0 0 196 143" preserveAspectRatio="none" aria-hidden="true">
        <path d="M0,143 C2,90 30,52 72,36 C88,30 94,16 95,0 C120,20 150,40 170,70 C188,96 196,118 196,143 Z" fill="var(--white)"/>
      </svg>
      <p class="scent-name display">Dunmoor</p>
      <p class="scent-note handwritten">Feisty<br>Energetic Soap</p>
    </div>
  </section>

</main>
</body>
</html>
```